Business card design for IT consulting company

Looking for a simple, modern, clean business card design.
Open to reworking our existing logo.

Attached is our current business cards which we do not like.
Ideally double sided with something simple on the back.
Rectangle / Horizonal only.
No rounded edges on the card.
White as the dominate color is preferred.

Target Market(s)

clients, legal, oil & gas, medical, professionals

Industry/Entity Type

IT, tech, consulting

Contact Information for Business Card

Name, Title, email, phone, cell, website

Font styles to use
Sans Serif

Requirements
Must have
• Clean design
Should not have
• loud colors or unusual fonts, etc

```html
<!DOCTYPE html>
<html lang="en">
<head>
<meta charset="utf-8">
<title>Qorvel Solutions – Business Card</title>
<link rel="stylesheet" href="https://fonts.googleapis.com/css2?family=Inter:wght@700&family=Montserrat:wght@500;700&family=Open+Sans:wght@400&display=swap">
<style>
  :root {
    --backdrop: #e3e3e3;
    --card-dark: #221f20;
    --card-light: #f3f3f3;
    --accent: #ecb52b;
    --ink: #1d1b1c;
    --paper-text: #f2f2f2;
  }
  * { margin: 0; padding: 0; box-sizing: border-box; }
  html, body { width: 1200px; height: 1200px; overflow: hidden; }
  body { background: var(--backdrop); position: relative; }

  .card {
    position: absolute;
    left: 234px;
    width: 731px;
    height: 418px;
    box-shadow: 0 10px 24px rgba(0,0,0,0.18);
  }
  .card--back { top: 160px; background: var(--card-dark); }
  .card--front { top: 631px; background: var(--card-light); }

  .brand { position: absolute; display: flex; align-items: center; }
  .brand__square { background: var(--accent); border-radius: 10px; flex: none; }
  .brand__name { font-family: "Inter", sans-serif; font-weight: 700; letter-spacing: -0.02em; white-space: nowrap; }

  .card--back .brand { left: 106px; top: 139px; }
  .card--back .brand__square { width: 140px; height: 140px; margin-right: 24px; border-radius: 12px; }
  .card--back .brand__name { font-size: 50px; color: var(--paper-text); }

  .website {
    position: absolute; left: 0; right: 0; top: 334px;
    text-align: center;
    font-family: "Open Sans", sans-serif; font-size: 23px;
    color: var(--accent);
  }

  .card--front .brand { left: 61px; top: 61px; }
  .card--front .brand__square { width: 92px; height: 92px; margin-right: 16px; border-radius: 8px; }
  .card--front .brand__name { font-size: 36px; color: var(--ink); }

  .person { position: absolute; left: 430px; top: 184px; right: 0; }
  .person__name {
    font-family: "Montserrat", sans-serif; font-weight: 700;
    font-size: 30px; color: var(--accent); line-height: 1;
  }
  .person__title {
    font-family: "Montserrat", sans-serif; font-weight: 500;
    font-size: 18px; color: var(--ink); margin-top: 10px;
  }
  .person__rule { height: 2px; background: var(--accent); margin-top: 12px; }

  .contacts { list-style: none; margin-top: 14px; }
  .contacts li {
    display: flex; align-items: center; height: 29.5px;
    font-family: "Open Sans", sans-serif; font-size: 18px; color: var(--ink);
  }
  .contacts svg { width: 16px; height: 16px; margin-right: 10px; flex: none; fill: var(--accent); }
</style>
</head>
<body>

<section class="card card--back">
  <div class="brand">
    <div class="brand__square"></div>
    <span class="brand__name">Qorvel Solutions</span>
  </div>
  <p class="website">www.qorvel.ca</p>
</section>

<section class="card card--front">
  <div class="brand">
    <div class="brand__square"></div>
    <span class="brand__name">Qorvel Solutions</span>
  </div>

  <div class="person">
    <h1 class="person__name">Dana Mercer</h1>
    <p class="person__title">IT Consultant</p>
    <div class="person__rule"></div>
    <ul class="contacts">
      <li>
        <svg viewBox="0 0 16 16" aria-hidden="true"><path d="M3.5 1.5l2.4 2.6-1.3 1.8c.9 2 2.5 3.6 4.5 4.5l1.8-1.3 2.6 2.4-1.6 2.2C6.8 13.4 2.6 9.2 1.3 3.1z"/></svg>
        (800) 555-0143
      </li>
      <li>
        <svg viewBox="0 0 16 16" aria-hidden="true"><path d="M4.5 1h7a1 1 0 0 1 1 1v12a1 1 0 0 1-1 1h-7a1 1 0 0 1-1-1V2a1 1 0 0 1 1-1zm.5 1.8v9.2h6V2.8zM8 12.6a.8.8 0 1 0 0 1.6.8.8 0 0 0 0-1.6z"/></svg>
        555.014.7729
      </li>
      <li>
        <svg viewBox="0 0 16 16" aria-hidden="true"><path d="M1 3.5h14v9H1zM1.8 4.3 8 9l6.2-4.7z" fill-rule="evenodd"/></svg>
        dana.mercer@qorvel.ca
      </li>
    </ul>
  </div>
</section>

</body>
</html>
```